REKEY 45.00 Special

We are a Home Warranty Company looking to do a few new postcards. I have attached a few samples of what we want one side to look like. The other side we will be doing a Special for January and February 2018. REKEY FOR ONLY $45.00 in January or February 2018 With any Home Warranty Order. 6 Key Holes & 4 Keys. * Homes outside of Locksmith Coverage area will be assessed a $40.00 fee in addition to the $45.00 fee. Not good with any other discounts. Also use our logo in the design and be creative. We like the WOW factor. The size need to be Parcelink Jumbo Card 11 x 6. Our web site is brightporchshield.com Remember one side will be our new design postcard that we sent samples and the other side will be the special. We are also looking for great new ideas for Home Warranty Postcards.

Target Market(s)

Real Estate Agents and Title Agents

Industry/Entity Type

Real Estate

Font styles to use
Serif

Colors
33b8a4
00a990
9bcb3c
abd036
86cfc6

Requirements
Must have
• OUR WEB SITE www.bpsquickform.com www.brightporchshield.com
• Our Phone # 800.614.2873 Our Logo
Nice to have
• Be creative, colorful

```html
<!DOCTYPE html>
<html lang="en">
<head>
<meta charset="utf-8">
<title>Home Warranty Plans</title>
<link href="https://fonts.googleapis.com/css2?family=Lato:wght@400;700;900&family=Roboto+Condensed:wght@700&display=swap" rel="stylesheet">
<style>
  :root {
    --teal: #00a990;
    --row-tint: #d6fbf6;
    --ink: #1a1a1a;
    --rule: #1f2a28;
    --green: #2ca94a;
    --page: #ececec;
    --card: #ffffff;
  }
  * { margin: 0; padding: 0; box-sizing: border-box; }
  html, body { width: 1200px; height: 1200px; overflow: hidden; background: var(--page); }
  .card-holder { position: absolute; left: 267px; top: 0; width: 666px; height: 1200px; overflow: hidden; }
  .card {
    width: 800px; height: 1442px; background: var(--card);
    transform: scale(0.8322); transform-origin: 0 0;
    position: relative; font-family: "Lato", sans-serif; color: var(--ink);
  }
  .plans {
    position: absolute; left: 30px; top: 30px; width: 736px;
    border-collapse: collapse; border: 2px solid var(--rule);
    table-layout: fixed;
  }
  .plans th {
    background: var(--teal); color: #fff; font-family: "Roboto Condensed", sans-serif;
    font-weight: 700; height: 73px; vertical-align: middle; text-align: center;
    border-left: 2px solid var(--rule); line-height: 1.15; font-size: 15px; letter-spacing: 0.3px;
  }
  .plans th .price { display: block; font-size: 25px; margin-top: 2px; }
  .plans th.plans-title {
    text-align: left; font-size: 26px; padding-left: 5px; border-left: none; line-height: 1.2;
  }
  .plans .spacer td { height: 10px; border-left: 2px solid var(--rule); }
  .plans .spacer td:first-child { border-left: none; }
  .plans tbody tr.item td { height: 34px; }
  .plans tbody tr.item:nth-child(odd) { background: var(--row-tint); }
  .plans tbody tr.item:nth-child(even) { background: #fff; }
  .plans td { border-left: 2px solid var(--rule); text-align: center; vertical-align: middle; }
  .plans td.feature {
    border-left: none; text-align: left; padding-left: 5px; font-size: 16px; white-space: nowrap;
  }
  .plans td.feature small { font-size: 15px; font-weight: 400; }
  .mark { font-weight: 900; font-size: 20px; }
  .note { position: absolute; left: 38px; top: 1308px; font-size: 16px; line-height: 23px; }
  .note b { font-weight: 700; }
  .contact { position: absolute; font-size: 16px; display: flex; align-items: center; gap: 10px; }
  .contact svg { width: 14px; height: 14px; flex: none; }
  .contact.phone { left: 38px; top: 1364px; font-weight: 700; }
  .contact.order { left: 38px; top: 1390px; }
  .contact.site { left: 254px; top: 1363px; }
  .contact.social { left: 254px; top: 1389px; }
  .brand { position: absolute; left: 566px; top: 1354px; display: flex; align-items: center; gap: 8px; }
  .brand-name { font-size: 16px; font-weight: 400; color: #3a3a3a; text-align: right; line-height: 17px; letter-spacing: 0.5px; }
  .brand-tag { display: block; font-size: 7px; letter-spacing: 1.5px; font-weight: 700; margin-top: 3px; }
  .brand-mark { width: 44px; height: 44px; background: var(--green); }
</style>
</head>
<body>
<div class="card-holder">
<div class="card">
  <table class="plans">
    <colgroup><col style="width:305px"><col style="width:103px"><col style="width:105px"><col style="width:113px"><col style="width:110px"></colgroup>
    <thead>
      <tr>
        <th class="plans-title">HOME WARRANTY PLANS<br>THAT’S RIGHT FOR YOU</th>
        <th>STANDARD<span class="price">$325</span></th>
        <th>STANDARD<br>PLUS<span class="price">$375</span></th>
        <th>PLUS<br>FAVORITE<span class="price">$400</span></th>
        <th>PREMIER<br>FAVORITE<span class="price">$475</span></th>
      </tr>
    </thead>
    <tbody>
      <tr class="spacer"><td></td><td></td><td></td><td></td><td></td></tr>
      <tr class="item"><td class="feature">Central Air Conditioner<small>-up to two systems</small></td><td></td><td class="mark">X</td><td class="mark">X</td><td class="mark">X</td></tr>
      <tr class="item"><td class="feature">Evaporative Coolers</td><td></td><td class="mark">X</td><td class="mark">X</td><td class="mark">X</td></tr>
      <tr class="item"><td class="feature">Central Heating <small>- up to two systems</small></td><td class="mark">X</td><td class="mark">X</td><td class="mark">X</td><td class="mark">X</td></tr>
      <tr class="item"><td class="feature">Boiler</td><td class="mark">X</td><td class="mark">X</td><td class="mark">X</td><td class="mark">X</td></tr>
      <tr class="item"><td class="feature">Thermostats</td><td class="mark">X</td><td class="mark">X</td><td class="mark">X</td><td class="mark">X</td></tr>
      <tr class="item"><td class="feature">Water Heater</td><td class="mark">X</td><td class="mark">X</td><td class="mark">X</td><td class="mark">X</td></tr>
      <tr class="item"><td class="feature">Tank less Water Heater</td><td class="mark">X</td><td class="mark">X</td><td class="mark">X</td><td class="mark">X</td></tr>
      <tr class="item"><td class="feature">Main Line Stoppages</td><td class="mark">X</td><td class="mark">X</td><td class="mark">X</td><td class="mark">X</td></tr>
      <tr class="item"><td class="feature">Plumbing Leaks</td><td class="mark">X</td><td class="mark">X</td><td class="mark">X</td><td class="mark">X</td></tr>
      <tr class="item"><td class="feature">Interior Waste Pipes</td><td class="mark">X</td><td class="mark">X</td><td class="mark">X</td><td class="mark">X</td></tr>
      <tr class="item"><td class="feature">Interior Hose Bibs</td><td class="mark">X</td><td class="mark">X</td><td class="mark">X</td><td class="mark">X</td></tr>
      <tr class="item"><td class="feature">Interior Water Lines</td><td class="mark">X</td><td class="mark">X</td><td class="mark">X</td><td class="mark">X</td></tr>
      <tr class="item"><td class="feature">Angle Stops and Gate Valves</td><td class="mark">X</td><td class="mark">X</td><td class="mark">X</td><td class="mark">X</td></tr>
      <tr class="item"><td class="feature">Toilet Wax Ring Seal</td><td class="mark">X</td><td class="mark">X</td><td class="mark">X</td><td class="mark">X</td></tr>
      <tr class="item"><td class="feature">Permanent Sump Pump</td><td class="mark">X</td><td class="mark">X</td><td class="mark">X</td><td class="mark">X</td></tr>
      <tr class="item"><td class="feature">Garbage Disposal</td><td class="mark">X</td><td class="mark">X</td><td class="mark">X</td><td class="mark">X</td></tr>
      <tr class="item"><td class="feature">Faucets</td><td class="mark">X</td><td class="mark">X</td><td class="mark">X</td><td class="mark">X</td></tr>
      <tr class="item"><td class="feature">Toilet (Parts)</td><td class="mark">X</td><td class="mark">X</td><td class="mark">X</td><td class="mark">X</td></tr>
      <tr class="item"><td class="feature">Electrical System</td><td class="mark">X</td><td class="mark">X</td><td class="mark">X</td><td class="mark">X</td></tr>
      <tr class="item"><td class="feature">Fuse Panel</td><td class="mark">X</td><td class="mark">X</td><td class="mark">X</td><td class="mark">X</td></tr>
      <tr class="item"><td class="feature">Circuit Breakers</td><td class="mark">X</td><td class="mark">X</td><td class="mark">X</td><td class="mark">X</td></tr>
      <tr class="item"><td class="feature">Electrical Switches</td><td class="mark">X</td><td class="mark">X</td><td class="mark">X</td><td class="mark">X</td></tr>
      <tr class="item"><td class="feature">Electrical Receptacles</td><td class="mark">X</td><td class="mark">X</td><td class="mark">X</td><td class="mark">X</td></tr>
      <tr class="item"><td class="feature">Garage Door Opener</td><td class="mark">X</td><td class="mark">X</td><td class="mark">X</td><td class="mark">X</td></tr>
      <tr class="item"><td class="feature">Central Vacuum</td><td class="mark">X</td><td class="mark">X</td><td class="mark">X</td><td class="mark">X</td></tr>
      <tr class="item"><td class="feature">Kitchen Exhaust Fans</td><td class="mark">X</td><td class="mark">X</td><td class="mark">X</td><td class="mark">X</td></tr>
      <tr class="item"><td class="feature">Range</td><td class="mark">X</td><td class="mark">X</td><td class="mark">X</td><td class="mark">X</td></tr>
      <tr class="item"><td class="feature">Oven</td><td class="mark">X</td><td class="mark">X</td><td class="mark">X</td><td class="mark">X</td></tr>
      <tr class="item"><td class="feature">Cooktop</td><td class="mark">X</td><td class="mark">X</td><td class="mark">X</td><td class="mark">X</td></tr>
      <tr class="item"><td class="feature">Built-in Microwave Oven</td><td class="mark">X</td><td class="mark">X</td><td class="mark">X</td><td class="mark">X</td></tr>
      <tr class="item"><td class="feature">Trash Compactor</td><td class="mark">X</td><td class="mark">X</td><td class="mark">X</td><td class="mark">X</td></tr>
      <tr class="item"><td class="feature">Metal Venting for Furnace</td><td class="mark">X</td><td class="mark">X</td><td class="mark">X</td><td class="mark">X</td></tr>
      <tr class="item"><td class="feature">Metal Venting for Water Heater</td><td class="mark">X</td><td class="mark">X</td><td class="mark">X</td><td class="mark">X</td></tr>
      <tr class="item"><td class="feature">Kitchen Refrigerator</td><td></td><td></td><td class="mark">X</td><td class="mark">X</td></tr>
      <tr class="item"><td class="feature">Washer and Dryer</td><td></td><td></td><td></td><td class="mark">X</td></tr>
    </tbody>
  </table>

  <p class="note"><b>VALUE-ADDED PASS THROUGH SERVICES</b>. provided at additional cost. No deductible required<br><b>*RE-KEY SERVICE</b></p>

  <div class="contact phone">
    <svg viewBox="0 0 14 14"><circle cx="7" cy="7" r="6" fill="none" stroke="#2ca94a" stroke-width="1.4"/><path d="M4.6 4.2l1.3-.3.7 1.6-.8.6a4.5 4.5 0 0 0 2.1 2.1l.6-.8 1.6.7-.3 1.3c-3 .2-5.4-2.2-5.2-5.2z" fill="#2ca94a"/></svg>
    <span>1-800-614-2873</span>
  </div>
  <div class="contact order">
    <svg viewBox="0 0 14 14"><circle cx="7" cy="7" r="6" fill="none" stroke="#2ca94a" stroke-width="1.3"/><path d="M1 7h12M7 1c-3 3-3 9 0 12M7 1c3 3 3 9 0 12" fill="none" stroke="#2ca94a" stroke-width="1"/></svg>
    <span>www.bpsquickform.com</span>
  </div>
  <div class="contact site">
    <svg viewBox="0 0 14 14"><circle cx="7" cy="7" r="6" fill="none" stroke="#2ca94a" stroke-width="1.3"/><path d="M1 7h12M7 1c-3 3-3 9 0 12M7 1c3 3 3 9 0 12" fill="none" stroke="#2ca94a" stroke-width="1"/></svg>
    <span>www.brightporchshield.com</span>
  </div>
  <div class="contact social">
    <svg viewBox="0 0 14 14"><circle cx="7" cy="7" r="6" fill="#2ca94a"/></svg>
    <span>/porchshieldplans</span>
  </div>

  <div class="brand">
    <div class="brand-name">BRIGHT PORCH<br>SHIELD<span class="brand-tag">HOME WARRANTY PLANS</span></div>
    <div class="brand-mark"></div>
  </div>
</div>
</div>
</body>
</html>
```